Cover-Design für Buch über Corona-Pandemie
Zielgruppe
Ich bin ein junger Arzt und schreibe ein Buch über die Corona Pandemie. Zielgruppe sind alle Menschen, die sich kritisch aber seriös mit der Thematik befassen. Ich werde das Buch selbst veröffentlichen über Buchwelt oder ähnliche Portale.
Aufgabenstellung
Sehr geehrte Designer,
ich hätte gern das Buchcover mit Vorderseite und Hinterseite. Die beiden Textvorlagen befinden sich in der hochgeladenen Datei. Seite 1 ist die Vorderseite, Seite 2 die Hinterseite des Buchcovers.
Sie können sich grob an dem Buchcover 'Fieber Irrtum' von Wendorf orientieren. Also ein sehr großer Titel in rot, schlicht gestaltet, unter dem Titel der Untertitel in schwarz, so wie in der angehängten Datei. Der Titel sollte ebenfalls auf zwei Zeilen in großer Schrift aufgeteilt sein wie von Wendorf. Der Autorenname sollte ganz unten auf der Coverseite zentral seinTitel, Untertitel und Autorenname sollten ca. 60% der Länge des Buchcovers ausmachen. Die Ähnlichkeit zum Wendorf Buch sollte wegen dem Urheberrecht nicht zu groß ist, aber da kennen Sie sich sicher besser aus und können sicher entsprechende Modifikationen machen. So kann man ja z.B Weinrot verwenden oder andere Formatierungen.
Darunter hätte ich gerne ein Gehirn, mit Injektionsspritzen, die in das Gehirn stechen und wie ein Kranz um das Gehirn gereiht sind Daneben sollte ein CoronaVirus sein, dessen Hülle dem Gehirn mit den Spritzen sehr ähnlich sieht. Beides in Schwarz-Weiß. Als grobe Orientierungshilfe habe ich selbst ein Gehirn mit den Spritzen in der Datei entworfen, damit Sie eine ungefähre Idee von der Optik haben.
Wenn Sie echte Abbildungen von Gehirn und Spritzen finden und sie in der Bildbearbeitung so nach meiner Vorlage gestalten können, wäre es am Schönsten. Sonst können sie einfach auch Symbole oder Comics wie ich verwenden, solange das Gehirn und das Virus optisch zusammenpassen und den gleichen Stil haben.
Sonst i Stil klare Linien, Minimalistisch.
Auf der Hinterseite des Cover sollte wie in der angehängten Datei das Zitat rot sein, der Text schwarz, sonst habe ich keine weiteren Wünsche.
Vielen Dank!
UPDATE: Zusätzliche hätte ich gerne ein Bild von mir und den Text über den Autor auf der Hinter..

```html
<!DOCTYPE html>
<html lang="de">
<head>
<meta charset="utf-8">
<title>Seuche Irrsinn? – Buchumschlag</title>
<link href="https://fonts.googleapis.com/css2?family=Raleway:wght@400;500;600;800&display=swap" rel="stylesheet">
<style>
  :root {
    --stage: #ef5a6c;
    --frame: #b9babd;
    --paper: #e9eaec;
    --ink: #1b1b1b;
    --red: #d8242f;
    --rule: #c9b7b9;
  }
  * { margin: 0; padding: 0; box-sizing: border-box; }
  html, body { width: 800px; height: 1200px; overflow: hidden; }
  body {
    background: var(--stage);
    font-family: "Raleway", sans-serif;
    color: var(--ink);
    position: relative;
  }
  .cover-spread {
    position: absolute;
    left: 20px; top: 337px;
    width: 760px; height: 526px;
    background: var(--frame);
    padding: 14px;
    box-shadow: 0 6px 18px rgba(0,0,0,.25);
  }
  .cover-paper {
    position: relative;
    width: 100%; height: 100%;
    background: var(--paper);
  }
  .spine-fold {
    position: absolute;
    left: 404px; top: 0; bottom: 0;
    width: 1px; background: var(--rule);
  }
  /* back cover */
  .back-quote {
    position: absolute;
    left: 28px; top: 42px; width: 270px;
    border-left: 2px solid var(--red);
    padding-left: 8px;
    color: var(--red);
    font-size: 9.5px; line-height: 13.5px; font-weight: 500;
  }
  .back-text {
    position: absolute;
    left: 24px; top: 105px; width: 276px;
    font-size: 9.5px; line-height: 13.5px;
    text-align: justify; hyphens: auto;
  }
  .back-text p + p { margin-top: 13px; }
  .author-photo {
    position: absolute;
    left: 24px; top: 362px;
    width: 60px; height: 68px;
    border: 2px solid #cfd0d3;
    background: linear-gradient(180deg, #d7dde6 0%, #b7c7dc 60%, #7f9cc4 100%);
  }
  .author-bio {
    position: absolute;
    left: 98px; top: 362px; width: 202px;
    font-size: 9.5px; line-height: 13.5px;
    text-align: justify; hyphens: auto;
  }
  /* spine */
  .spine-title {
    position: absolute;
    left: 356px; top: 65px;
    writing-mode: vertical-rl;
    color: var(--red);
    font-weight: 800; font-size: 16px; line-height: 18px; letter-spacing: 1px;
  }
  .spine-author {
    position: absolute;
    left: 362px; top: 250px;
    writing-mode: vertical-rl;
    font-size: 12.5px; font-weight: 500;
  }
  /* front cover */
  .front {
    position: absolute;
    left: 405px; top: 0; right: 0; bottom: 0;
    text-align: center;
  }
  .front-title {
    margin-top: 42px;
    color: var(--red);
    font-weight: 800;
    line-height: 1;
  }
  .front-title .line-1 { display: block; font-size: 60px; letter-spacing: 4px; }
  .front-title .line-2 { display: block; font-size: 40px; letter-spacing: 4px; margin-top: 6px; }
  .front-subtitle {
    margin-top: 24px;
    font-size: 14.5px; line-height: 20px; font-weight: 500;
  }
  .brain-illustration {
    position: absolute;
    left: 68px; top: 250px;
    width: 218px; height: 166px;
    border-radius: 50%;
    background: radial-gradient(ellipse at center, #d9414b 0%, #cf3a44 45%, #c9d4e0 70%, var(--paper) 100%);
  }
  .front-author {
    position: absolute;
    left: 0; right: 0; bottom: 10px;
    font-size: 19px; font-weight: 500;
  }
</style>
</head>
<body>
  <section class="cover-spread">
    <div class="cover-paper">
      <div class="back-quote">„Die bewusste und zielgerichtete Manipulation der Verhaltensweisen und Einstellungen der Massen ist ein wesentlicher Bestandteil westlicher Demokratien.“</div>
      <div class="back-text">
        <p>Schon der Begründer der Public Relations und Neffe von Siegfried Frohner, Eduard Bergmann, erkannte 1928 die zentrale Rolle des Meinungsmanagements, das aktueller denn je ist.</p>
        <p>Die Pandemie reißt gewaltige Gräben innerhalb unserer Gesellschaft auf. Emotionalisierung, Moralisierung und Manipulation vergiften die inhaltliche Diskussion von Mensch zu Mensch, die Basis von Wissenschaft, Demokratie und Beziehungen. Dieser verzerrte Diskurs verlegt Lösungswege aus der Pandemie.</p>
        <p>Das Buch zeigt viele etablierte Manipulationstechniken, die seit Jahrzehnten von Politik, Medien und Wirtschaft angewendet werden, um die öffentliche Meinung zu beeinflussen. Außerdem beleuchtet es logische Fehlschlüsse, die viele Argumentationen ungültig machen.</p>
      </div>
      <div class="author-photo" role="img" aria-label="Porträtfoto des Autors"></div>
      <div class="author-bio">Jonas Wieland, geboren 1992 in der Obersteiermark, arbeitet als Arzt in Ausbildung zum Allgemeinmediziner in einer Wiener Klinik. Er erlebt als junger Mediziner die Coronapandemie an vorderster Front.</div>

      <div class="spine-title">SEUCHE<br>IRRSINN?</div>
      <div class="spine-author">Dr. med. univ. Jonas Wieland</div>
      <div class="spine-fold"></div>

      <div class="front">
        <h1 class="front-title"><span class="line-1">SEUCHE</span><span class="line-2">IRRSINN?</span></h1>
        <p class="front-subtitle">Wie Meinungslenkung und logische<br>Trugschlüsse unser Urteil vergiften</p>
        <div class="brain-illustration" role="img" aria-label="Illustration: rotes Gehirn, kranzförmig umgeben von Injektionsspritzen"></div>
        <p class="front-author">Dr. med. univ. Jonas Wieland</p>
      </div>
    </div>
  </section>
</body>
</html>
```